LAW FIRM - RE-DESIGN - (professional, excellence, tradition and innovation)

We are a premier law firm in New South Wales, Australia. We pride ourselves on being cutting edge and up to date in our market.

Our firm formed in 1874 and has a particularly strong tradition within it's geographic footprint. acting for clients over multiple generations. Despite our regional background, our reputation for excellence has enable us to remain highly visible in a large area.

We have invested heavily in ensuring future planning of this business, and do so on a recurring basis. This has lead to a review of our existing web site.

Although serviceable we feel our previous website is out-of-date and not as in touch with the modern market. We are aware that for the emerging clients a web site is often the face of a firm and a failure to hold attention on the first page may fail to capture the client.

We are seeking designs to communicate the core values of professionalism and excellence. At the same time as maintaining traditional country values of honesty, integrity and hard work we strive to embrace changes to the law and technology.

Target Market(s)

Clients of Law Firm

Industry/Entity Type

Law Firm

Coding

Coded - Design and coding required

Number of Pages Required

5+ page

Requirements
Must have
• A strong sense of professionalism and excellence with a careful balance between traditional values and innovation.
Nice to have
• We have included within our design brief links to top competitors sites to assist for design concepts.

```html
<!DOCTYPE html>
<html lang="en">
<head>
<meta charset="utf-8">
<title>HCB Law</title>
<link href="https://fonts.googleapis.com/css2?family=Lato:wght@400;700;900&family=Open+Sans:wght@400;600;700&display=swap" rel="stylesheet">
<style>
:root{
  --navy:#0d3a78;
  --navy-deep:#0b2d5e;
  --ink:#222;
  --body:#444;
  --soft:#eef1f6;
  --line:#c9ced6;
  --white:#fff;
  --footer:#f2f2f2;
}
*{box-sizing:border-box;margin:0;padding:0}
html,body{width:1200px;height:3333px;overflow:hidden}
body{font-family:"Open Sans",Arial,sans-serif;color:var(--body);background:var(--white);position:relative}
.section{position:absolute;left:0;width:1200px}
.title{font-family:"Lato",Arial,sans-serif;font-weight:700;color:var(--navy);font-size:27px;text-align:center;letter-spacing:.3px}
.rule{width:140px;height:2px;background:var(--navy);margin:16px auto 0}

/* hero */
.hero{top:0;height:635px;overflow:hidden}
.hero-photo{position:absolute;inset:0;background:linear-gradient(180deg,#0d1f3d 0%,#1d3a66 35%,#2b4970 55%,#1a2a45 75%,#0b1526 100%)}
.topbar{position:absolute;top:22px;right:100px;display:flex;gap:28px;color:var(--white);font-size:15px}
.topbar span{display:flex;align-items:center;gap:10px}
.topbar svg{width:28px;height:28px}
.brand{position:absolute;top:40px;left:100px;color:var(--white);font-family:"Lato",Arial,sans-serif;font-weight:700;font-size:36px;display:flex;align-items:center;gap:10px}
.brand i{width:14px;height:14px;background:var(--white);display:block}
.nav{position:absolute;top:86px;right:100px;display:flex;gap:44px;font-family:"Lato",Arial,sans-serif;font-weight:700;font-size:15px;color:var(--white)}
.hero h1{position:absolute;top:232px;width:100%;text-align:center;font-family:"Lato",Arial,sans-serif;font-weight:900;font-size:50px;color:var(--white)}
.hero p{position:absolute;top:322px;left:280px;width:640px;text-align:center;color:var(--white);font-size:16px;line-height:24px}
.btn-hero{position:absolute;top:427px;left:529px;width:142px;height:56px;border:2px solid var(--white);color:var(--white);font-family:"Lato",Arial,sans-serif;font-weight:700;font-size:15px;display:flex;align-items:center;justify-content:center}
.tab{position:absolute;bottom:-60px;left:490px;width:220px;height:120px;background:var(--white);border-radius:50%}
.dots{position:absolute;bottom:12px;left:553px;display:flex;gap:6px}
.dots span{width:14px;height:14px;border:2px solid var(--navy);border-radius:50%}
.dots span:first-child{background:var(--navy)}

/* about */
.about{top:635px;height:520px;padding-top:68px}
.about .lead{width:820px;margin:50px auto 0;text-align:center;font-weight:600;color:var(--ink);font-size:15px;line-height:26px}
.about .copy{width:1000px;margin:20px auto 0;text-align:center;font-size:12.5px;line-height:21px}
.about .copy+.copy{margin-top:12px}
.btn-row{display:flex;justify-content:center;gap:12px;margin-top:30px}
.btn{width:116px;height:42px;display:flex;align-items:center;justify-content:center;font-size:14px;font-weight:600}
.btn-solid{background:var(--navy);color:var(--white)}
.btn-outline{border:2px solid var(--ink);color:var(--ink)}

/* partners */
.partners{top:1155px;height:478px;background:var(--soft);padding-top:56px}
.people{display:flex;justify-content:center;gap:28px;margin-top:70px}
.person{width:182px;text-align:center}
.portrait{width:122px;height:122px;border-radius:50%;border:3px solid var(--navy);margin:0 auto;box-shadow:inset 0 0 0 4px var(--white);background:radial-gradient(circle at 50% 40%,#b08a66 0%,#6a4a33 45%,#2c241f 100%)}
.person h3{font-family:"Lato",Arial,sans-serif;font-weight:700;color:var(--navy);font-size:16px;margin-top:18px}
.person p{font-size:11.5px;line-height:17px;margin-top:10px}

/* services */
.services{top:1633px;height:542px;color:var(--white);overflow:hidden}
.services-photo{position:absolute;inset:0;background:linear-gradient(90deg,#0d3570 0%,#1b4a86 45%,#24548f 60%,#0d3570 100%)}
.services .title{color:var(--white);position:relative;margin-top:70px}
.services .rule{background:var(--white);position:relative;width:200px}
.svc-grid{position:absolute;top:205px;left:100px;width:1000px;display:grid;grid-template-columns:1fr 1fr;column-gap:40px;row-gap:36px}
.svc{display:flex;gap:22px}
.svc svg{width:80px;height:80px;flex:none}
.svc h3{font-family:"Lato",Arial,sans-serif;font-weight:700;font-size:22px}
.svc p{font-size:12.5px;line-height:22px;margin-top:12px;width:370px}

/* testimonials */
.testimonials{top:2175px;height:488px;padding-top:66px}
.quotes{position:absolute;top:195px;left:98px;display:flex;gap:20px}
.quote{width:323px;position:relative}
.quote-box{height:194px;border:2px solid var(--navy);padding:52px 20px 0;font-size:13px;line-height:24px;color:var(--ink);position:relative}
.quote-box::after{content:"";position:absolute;left:-2px;bottom:-22px;border-left:22px solid var(--navy);border-bottom:22px solid transparent}
.quote.active .quote-box{background:var(--navy);color:var(--white)}
.quote-icon{position:absolute;top:-18px;left:142px;width:38px;height:38px;border-radius:50%;background:var(--navy);border:3px solid var(--white);z-index:2;display:flex;align-items:center;justify-content:center}
.quote.active .quote-icon{background:var(--white);border-color:var(--navy)}
.quote cite{display:block;font-style:normal;font-size:14px;font-weight:600;color:var(--ink);margin-top:32px;padding-left:30px}
.quote.active cite{color:var(--navy)}
.arrow{position:absolute;top:270px}
.arrow svg{width:20px;height:36px}

/* community */
.community{top:2663px;height:245px}
.community .divider{position:absolute;top:0;left:98px;width:1004px;height:3px;background:var(--navy)}
.community h2{position:absolute;top:78px;left:98px;font-family:"Lato",Arial,sans-serif;font-weight:700;color:var(--navy);font-size:25px}
.community p{position:absolute;top:130px;left:98px;width:360px;font-size:13px;line-height:24px}
.community .vline{position:absolute;top:60px;left:498px;width:2px;height:175px;background:var(--line)}
.sponsor{position:absolute;top:80px;width:250px;height:104px;border:1px solid var(--line);display:flex;align-items:center;justify-content:center}
.sponsor span{width:60px;height:60px;background:#d8dbe0;border-radius:50%}
.sponsor.second span{width:110px;height:34px;border-radius:4px}

/* footer */
.footer{top:2908px;height:425px;background:var(--footer);border-top:6px solid var(--navy-deep)}
.footer .logo{position:absolute;top:146px;left:112px;font-family:"Lato",Arial,sans-serif;font-weight:700;font-size:44px;color:var(--navy)}
.footer h4{position:absolute;top:66px;left:380px;font-family:"Lato",Arial,sans-serif;font-weight:700;font-size:17px;color:var(--navy);letter-spacing:.5px}
.offices{position:absolute;top:120px;left:380px;display:flex}
.office{width:282px}
.row{display:flex;gap:18px;height:64px;margin-bottom:0}
.ico{width:38px;height:38px;border:2px solid var(--navy);border-radius:50%;flex:none;display:flex;align-items:center;justify-content:center}
.ico svg{width:18px;height:18px}
.row b{display:block;font-size:14px;color:var(--ink);font-weight:700}
.row small{display:block;font-size:12.5px;line-height:20px;color:var(--body);margin-top:4px}
.footer .base{position:absolute;top:365px;left:98px;width:1004px;border-top:1px solid var(--line);padding-top:18px;display:flex;justify-content:space-between;align-items:center;font-size:13.5px;color:var(--ink)}
.social{display:flex;gap:12px}
.social span{width:34px;height:34px;border:2px solid var(--ink);border-radius:50%}
</style>
</head>
<body>

<header class="section hero">
  <div class="hero-photo" role="img" aria-label="Night view of a harbour city skyline with an opera house and bridge reflected in the water"></div>
  <div class="brand"><i></i>HCB Law</div>
  <div class="topbar">
    <span><svg viewBox="0 0 28 28" fill="none" stroke="#fff" stroke-width="1.5"><circle cx="14" cy="14" r="12.5"/><rect x="8" y="10" width="12" height="8"/><path d="M8 10l6 5 6-5"/></svg>info@hcblaw.com.au</span>
    <span><svg viewBox="0 0 28 28" fill="none" stroke="#fff" stroke-width="1.5"><circle cx="14" cy="14" r="12.5"/><path d="M10 8c-1 3 2 9 7 11l2-2-2-2-2 1c-1-1-2-2-3-4l1-2-2-2z"/></svg>02 5550 1400</span>
  </div>
  <nav class="nav"><span>HOME</span><span>ABOUT US</span><span>SERVICES</span><span>OUR PEOPLE</span><span>FAQ'S</span><span>CONTACT US</span></nav>
  <h1>WELCOME TO HCB LAW</h1>
  <p>Since that time HCB Law has maintained a dominant presence. Additionally, although this firm has its genesis within the Eastvale region.</p>
  <div class="btn-hero">READ MORE</div>
  <div class="tab"></div>
  <div class="dots"><span></span><span></span><span></span><span></span><span></span></div>
</header>

<section class="section about">
  <h2 class="title">ABOUT HCB LAW</h2>
  <div class="rule"></div>
  <p class="lead">HCB Law (formerly known as Hale Crane &amp; Barlow) has been part of the Eastvale Region of New South Wales for over a century.</p>
  <p class="copy">HCB Law has been in existence since 1874 originally starting out as the firm Arthur Winslow of Kestrel Creek. In 1894 Arthur Winslow was acquired by Colonel RT Hale. The firm became known as JW Hale &amp; Co. until early 1970 when it became Hale &amp; Co, Hale Crane &amp; Co in 1979 and Hale Crane &amp; Barlow in 1982.</p>
  <p class="copy">HCB Law is proud of its long and distinguished history as a regional law firm and its service to the region. In December 1999, the firm opened an office in Marlow Falls taking over the practice of LM Fenwick &amp; Associates. This was followed by the incorporation of Ashdown &amp; Co in December 2000 and the Brookhaven office moved to larger premises in Carrick Street.</p>
  <div class="btn-row"><span class="btn btn-solid">Read More</span><span class="btn btn-outline">Contact Us</span></div>
</section>

<section class="section partners">
  <h2 class="title">PARTNERS OF HCB LAW</h2>
  <div class="rule"></div>
  <div class="people">
    <div class="person"><div class="portrait" role="img" aria-label="Portrait photo of partner David Crane"></div><h3>David Crane</h3><p>Currently the senior partner of HCB Law, David Crane was admitted as a solicitor.</p></div>
    <div class="person"><div class="portrait" role="img" aria-label="Portrait photo of partner Ross Barlow"></div><h3>Ross Barlow</h3><p>As senior partner of HCB Law along side David Crane, Ross was admitted as a solicitor.</p></div>
    <div class="person"><div class="portrait" role="img" aria-label="Portrait photo of partner Helen Crane"></div><h3>Helen Crane</h3><p>Helen Crane was admitted as a solicitor in July 2006 after completing her degrees.</p></div>
    <div class="person"><div class="portrait" role="img" aria-label="Portrait photo of partner Victor Lam"></div><h3>Victor Lam</h3><p>Victor joining HCB Law in March 2006 and was admitted as a solicitor in July 2006.</p></div>
    <div class="person"><div class="portrait" role="img" aria-label="Portrait photo of partner Nina Walsh"></div><h3>Nina Walsh</h3><p>Nina was admitted to practice as a Solicitor in July 2002 after completing a Bachelor of Commerce.</p></div>
  </div>
</section>

<section class="section services">
  <div class="services-photo" role="img" aria-label="Blue-tinted photo of lawyers meeting in an office"></div>
  <h2 class="title">OUR LAW FIRM SERVICES</h2>
  <div class="rule"></div>
  <div class="svc-grid">
    <div class="svc">
      <svg viewBox="0 0 80 80" fill="none" stroke="#fff" stroke-width="2.5"><circle cx="40" cy="16" r="11"/><path d="M40 27v10"/><path d="M6 58l17-14 17 14M40 58l17-14 17 14"/><path d="M11 55v18h24V55M45 55v18h24V55"/></svg>
      <div><h3>Building &amp; Construction</h3><p>Our team can help draft and advise on building contracts for a home, commercial or industrial buildings, as well as represent on contracts to be negotiated or in the event of a dispute.</p></div>
    </div>
    <div class="svc">
      <svg viewBox="0 0 80 80" fill="#fff"><circle cx="26" cy="14" r="8"/><rect x="16" y="25" width="20" height="40" rx="3"/><rect x="44" y="30" width="3" height="36"/><rect x="34" y="30" width="24" height="3"/><path d="M32 46l4-12 4 12z M52 46l4-12 4 12z"/><rect x="38" y="64" width="16" height="4"/></svg>
      <div><h3>Criminal Law</h3><p>Our team can help draft and advise on building contracts for a home, commercial or industrial buildings, as well as represent on contracts to be negotiated or in the event of a dispute.</p></div>
    </div>
    <div class="svc">
      <svg viewBox="0 0 80 80" fill="none" stroke="#fff" stroke-width="2.5"><rect x="12" y="18" width="56" height="36" rx="2"/><path d="M4 60h72l-4 6H8z"/><path d="M30 42l10-9 10 9M33 40v8h14v-8"/></svg>
      <div><h3>Corporate &amp; Commercial</h3><p>Our team can help draft and advise on building contracts for a home, commercial or industrial buildings, as well as represent on contracts to be negotiated or in the event of a dispute.</p></div>
    </div>
    <div class="svc">
      <svg viewBox="0 0 80 80" fill="#fff"><path d="M40 8l22 14H18z"/><rect x="20" y="24" width="40" height="6"/><rect x="24" y="34" width="32" height="22" fill="none" stroke="#fff" stroke-width="3"/><rect x="34" y="40" width="12" height="10"/><rect x="18" y="60" width="44" height="6"/><rect x="14" y="68" width="52" height="5"/></svg>
      <div><h3>Family Law</h3><p>Our team can help draft and advise on building contracts for a home, commercial or industrial buildings, as well as represent on contracts to be negotiated or in the event of a dispute.</p></div>
    </div>
  </div>
</section>

<section class="section testimonials">
  <h2 class="title">CLIENT TESTIMONIALS</h2>
  <div class="rule"></div>
  <div class="arrow" style="left:38px"><svg viewBox="0 0 20 36" fill="none" stroke="#555" stroke-width="2"><path d="M18 2L2 18l16 16"/></svg></div>
  <div class="arrow" style="right:38px"><svg viewBox="0 0 20 36" fill="none" stroke="#555" stroke-width="2"><path d="M2 2l16 16L2 34"/></svg></div>
  <div class="quotes">
    <div class="quote">
      <div class="quote-icon"><svg width="18" height="16" viewBox="0 0 18 16" fill="#fff"><ellipse cx="9" cy="7" rx="8" ry="6"/><path d="M4 11l-2 5 6-3z"/></svg></div>
      <div class="quote-box">“Able to distil complex legal issues into advice which is easy to digest and to implement. Very impressive. The team shows amazing energy and outstanding dedication.”</div>
      <cite>- Whitfield</cite>
    </div>
    <div class="quote active">
      <div class="quote-icon"><svg width="18" height="16" viewBox="0 0 18 16" fill="#0d3a78"><ellipse cx="9" cy="7" rx="8" ry="6"/><path d="M4 11l-2 5 6-3z"/></svg></div>
      <div class="quote-box">“Able to distil complex legal issues into advice which is easy to digest and to implement. Very impressive. The team shows amazing energy and outstanding dedication.”</div>
      <cite>- Paul Harding</cite>
    </div>
    <div class="quote">
      <div class="quote-icon"><svg width="18" height="16" viewBox="0 0 18 16" fill="#fff"><ellipse cx="9" cy="7" rx="8" ry="6"/><path d="M4 11l-2 5 6-3z"/></svg></div>
      <div class="quote-box">“Able to distil complex legal issues into advice which is easy to digest and to implement. Very impressive. The team shows amazing energy and outstanding dedication.”</div>
      <cite>- Donovan</cite>
    </div>
  </div>
</section>

<section class="section community">
  <div class="divider"></div>
  <h2>OUR COMMUNITY</h2>
  <p>HCB Law is proud to support and be part of these great community events and programs.</p>
  <div class="vline"></div>
  <div class="sponsor" style="left:552px"><span></span></div>
  <div class="sponsor second" style="left:852px"><span></span></div>
</section>

<footer class="section footer">
  <div class="logo">HCB Law</div>
  <h4>CONTACT US</h4>
  <div class="offices">
    <div class="office">
      <div class="row"><span class="ico"><svg viewBox="0 0 18 18" fill="none" stroke="#0d3a78" stroke-width="1.6"><path d="M9 17s6-6 6-10A6 6 0 003 7c0 4 6 10 6 10z"/><circle cx="9" cy="7" r="2"/></svg></span><div><b>BROOKHAVEN,</b><small>Suite 9, Merrow Arcade<br>Brookhaven, NSW 2398</small></div></div>
      <div class="row"><span class="ico"><svg viewBox="0 0 18 18" fill="none" stroke="#0d3a78" stroke-width="1.6"><rect x="5" y="1" width="8" height="16" rx="1.5"/><path d="M8 14h2"/></svg></span><div><b>PHONE:</b><small>02 5550 1400</small></div></div>
      <div class="row"><span class="ico"><svg viewBox="0 0 18 18" fill="none" stroke="#0d3a78" stroke-width="1.6"><rect x="2" y="7" width="14" height="9" rx="1"/><path d="M5 7V2h8v5"/><path d="M5 11h8"/></svg></span><div><b>FAX:</b><small>02 5550 1433</small></div></div>
    </div>
    <div class="office">
      <div class="row"><span class="ico"><svg viewBox="0 0 18 18" fill="none" stroke="#0d3a78" stroke-width="1.6"><path d="M9 17s6-6 6-10A6 6 0 003 7c0 4 6 10 6 10z"/><circle cx="9" cy="7" r="2"/></svg></span><div><b>KESTREL CREEK,</b><small>218 Lindell Street<br>Kestrel Creek NSW 2394</small></div></div>
      <div class="row"><span class="ico"><svg viewBox="0 0 18 18" fill="none" stroke="#0d3a78" stroke-width="1.6"><rect x="5" y="1" width="8" height="16" rx="1.5"/><path d="M8 14h2"/></svg></span><div><b>PHONE:</b><small>02 5550 2200</small></div></div>
      <div class="row"><span class="ico"><svg viewBox="0 0 18 18" fill="none" stroke="#0d3a78" stroke-width="1.6"><rect x="2" y="7" width="14" height="9" rx="1"/><path d="M5 7V2h8v5"/><path d="M5 11h8"/></svg></span><div><b>FAX:</b><small>02 5550 2244</small></div></div>
    </div>
    <div class="office">
      <div class="row"><span class="ico"><svg viewBox="0 0 18 18" fill="none" stroke="#0d3a78" stroke-width="1.6"><path d="M9 17s6-6 6-10A6 6 0 003 7c0 4 6 10 6 10z"/><circle cx="9" cy="7" r="2"/></svg></span><div><b>KESTREL CREEK,</b><small>74 Ormond Street<br>Ridgeway NSW 2391</small></div></div>
      <div class="row"><span class="ico"><svg viewBox="0 0 18 18" fill="none" stroke="#0d3a78" stroke-width="1.6"><rect x="5" y="1" width="8" height="16" rx="1.5"/><path d="M8 14h2"/></svg></span><div><b>PHONE:</b><small>02 5550 1400</small></div></div>
    </div>
  </div>
  <div class="base">
    <span>Copyright © 2017 HCB Law. All Right Reserved</span>
    <div class="social"><span></span><span></span><span></span><span></span><span></span></div>
  </div>
</footer>

</body>
</html>
```